Family Ranch with a hobby vineyard needs 2 wine labels for our first harvest

Design 2 wine labels (front and back) with the Brindor Ranch logo.
Label 1:
Sauvignon Blanc
Alc. 12.5% by Vol.
Palos Verdes Peninsula - add as the region
Year 2022
Label 2:
Cabernet Sauvignon
Alc. 13.5% by Vol.
Year 2022
For the back label design:
GOVERNMENT WARNING: (1) According to the Surgeon General, women
should not drink alcoholic beverages during pregnancy because of the risk of
birth defects. (2) Consumption of alcoholic beverages impairs your ability to
drive a car or operate machinery, and may cause health problems.
Contains Sulfates.
750ML
I just received the bottles and have attached a picture.
Look and feel
Each slider illustrates characteristics of the customer's brand and the style your logo design should communicate.

```html
<!DOCTYPE html>
<html lang="en">
<head>
<meta charset="utf-8">
<title>Brindor Ranch – Wine Labels</title>
<link href="https://fonts.googleapis.com/css2?family=Poppins:wght@300;400;500;600&display=swap" rel="stylesheet">
<style>
  :root {
    --bg: #000000;
    --paper: #ffffff;
    --ink: #111111;
    --title: #ffffff;
  }
  * { margin: 0; padding: 0; box-sizing: border-box; }
  html, body { width: 1200px; height: 1000px; overflow: hidden; background: var(--bg); }
  body { position: relative; font-family: "Poppins", sans-serif; color: var(--ink); }

  .panel-title {
    position: absolute; top: 286px; width: 240px; margin-left: -120px;
    text-align: center; color: var(--title); font-size: 21px; font-weight: 400;
  }

  .front-label { position: absolute; top: 336px; width: 181px; height: 372px; }
  .front-label svg.label-shape { position: absolute; inset: 0; }
  .label-1 { left: 239px; }
  .label-2 { left: 514px; }

  .back-label { position: absolute; left: 790px; top: 357px; width: 160px; height: 329px;
    background: var(--paper); border-radius: 11px; }
  .back-frame { position: absolute; left: 12px; top: 12px; width: 136px; height: 305px;
    border: 1.2px solid var(--ink); border-radius: 4px; }

  .centered { position: absolute; left: 0; width: 100%; text-align: center; }

  .brand-dot { position: absolute; left: 50%; top: 37px; width: 40px; height: 40px;
    margin-left: -20px; border-radius: 50%; background: var(--ink); }
  .tagline { top: 86px; font-size: 9.5px; font-weight: 500; letter-spacing: 1.4px; }

  .brand-name { font-weight: 600; line-height: 1; color: var(--ink); }
  .brand-name .main { display: block; font-size: 25px; letter-spacing: -0.3px; }
  .brand-name .sub { display: block; font-size: 9.5px; letter-spacing: 5px; margin-top: 3px; padding-left: 5px; }
  .front-label .brand-name { top: 166px; }
  .back-label .brand-name { top: 79px; }

  .wine-details { top: 274px; font-size: 5px; line-height: 5.5px; font-weight: 300; }
  .volume { font-size: 10px; font-weight: 500; }
  .front-label .volume { top: 328px; }
  .back-label .volume { top: 298px; }

  .warning-title { top: 165px; font-size: 8.5px; font-weight: 500; letter-spacing: 0.2px; }
  .warning-text { top: 186px; padding: 0 28px; font-size: 5px; line-height: 5.6px; font-weight: 300; }
  .warning-text p + p { margin-top: 5px; }
  .sulfites { top: 255px; font-size: 5px; font-weight: 300; }
</style>
</head>
<body>

  <h2 class="panel-title" style="left:330px">Labels 1 Front</h2>
  <h2 class="panel-title" style="left:605px">Labels 2 Front</h2>
  <h2 class="panel-title" style="left:870px">Back</h2>

  <section class="front-label label-1">
    <svg class="label-shape" width="181" height="372" viewBox="0 0 181 372">
      <path fill="#fff" d="M0,38 C30,38 45,25 60,15 C75,4 82,0 90.5,0 C99,0 106,4 121,15 C136,25 151,38 181,38 L181,371 C140,359 115,358 90.5,358 C66,358 41,359 0,371 Z"/>
      <path fill="none" stroke="#111" stroke-width="1" d="M12,49 C35,47 50,35 62,24 C75,14 80,11 90.5,11 C101,11 106,14 119,24 C131,35 146,47 169,49 L169,355 C130,348 110,346 90.5,346 C71,346 51,348 12,355 Z"/>
    </svg>
    <div class="brand-dot"></div>
    <p class="centered tagline">PREMIUM PRODUCT</p>
    <p class="centered brand-name"><span class="main">BRINDOR</span><span class="sub">RANCH</span></p>
    <p class="centered wine-details">Sauvignon Blanc<br>Alc. 12.5% by Vol.<br>Palos Verdes Peninsula - add as the region<br>Year 2022</p>
    <p class="centered volume">750ML</p>
  </section>

  <section class="front-label label-2">
    <svg class="label-shape" width="181" height="372" viewBox="0 0 181 372">
      <path fill="#fff" d="M0,38 C30,38 45,25 60,15 C75,4 82,0 90.5,0 C99,0 106,4 121,15 C136,25 151,38 181,38 L181,371 C140,359 115,358 90.5,358 C66,358 41,359 0,371 Z"/>
      <path fill="none" stroke="#111" stroke-width="1" d="M12,49 C35,47 50,35 62,24 C75,14 80,11 90.5,11 C101,11 106,14 119,24 C131,35 146,47 169,49 L169,355 C130,348 110,346 90.5,346 C71,346 51,348 12,355 Z"/>
    </svg>
    <div class="brand-dot"></div>
    <p class="centered tagline">PREMIUM PRODUCT</p>
    <p class="centered brand-name"><span class="main">BRINDOR</span><span class="sub">RANCH</span></p>
    <p class="centered wine-details">Cabernet Sauvignon<br>Alc. 13.5% by Vol.<br>Palos Verdes Peninsula - add as the region<br>Year 2022</p>
    <p class="centered volume">750ML</p>
  </section>

  <section class="back-label">
    <div class="back-frame"></div>
    <p class="centered brand-name"><span class="main">BRINDOR</span><span class="sub">RANCH</span></p>
    <p class="centered warning-title">GOVERNMENT WARNING</p>
    <div class="centered warning-text">
      <p>(1) According to the Surgeon General, women should not drink alcoholic beverages during pregnancy because of the risk of birth defects.</p>
      <p>(2) Consumption of alcoholic beverages impairs your ability to drive a car or operate machinery, and may cause health problems.</p>
    </div>
    <p class="centered sulfites">Contains Sulfates.</p>
    <p class="centered volume">750ML</p>
  </section>

</body>
</html>
```